Email & signature design template

My company sells photo ID and plastic card products. I would like a new email design template that reflects our focus on secure, smart, ID cards. Like your Government ID card, only with a bit more bling (colour). Using guilloche patterns and similar security feature design perhaps even hologram type effect from credit cards would be great. FOCUS ON THE SIGNATURE. No fancy background graphics making email hard to read. File size needs to be kept to a minimum and black and white email for possible printing is also preferred. Needs to include space for employee photo. Name, telephone number, optional mobile number and email address. As well as a reminder to save our trees and only print this email if absolutely necessary would be nice. Also space for ratings buttons and T&C's. I have attached our current design which I am not to fond of. Also a copy of a VERY old one which we liked much more but was impossible to automate with slanting text not being an option outside of making it part of an image. Traditionally our CI colours were orange and grey like that found on the logo copy attached. You are welcome to design complimentary to those colours. Hope that's good enough to let you have fun coming up with the proposals.

Target Market(s)

Business people in Government, IT and security markets.

Font styles to use
Serif

Colors
0692cd
0255a3
f04a50

Requirements
Must have
• Like your Government ID card, only with a bit more bling (colour). Using guilloche patterns and similar security feature design perhaps even hologram type effect from credit cards would be great. FOCUS ON THE SIGNATURE.
• employee photo. Name, telephone number, optional mobile number and email address.
Nice to have
• As well as a reminder to save our trees and only print this email if absolutely necessary would be nice.
• hologram type effect from credit cards would be great.
Should not have
• Text at angles.
• Dark or difficult background for main email layout to make it difficult to read.
• Signature can be any colours. Still be easy to read.

```html
<!DOCTYPE html>
<html lang="en">
<head>
<meta charset="utf-8">
<title>Email Signature – Keystone ID Solutions</title>
<link rel="stylesheet" href="https://fonts.googleapis.com/css2?family=Montserrat:ital,wght@0,400;0,500;0,600;0,700;1,400&family=Roboto+Condensed:wght@400&display=swap">
<style>
  :root {
    --stage: #e2e2e2;
    --paper: #ffffff;
    --panel: #e8e8e8;
    --photo: #cbcbcb;
    --orange: #f7941e;
    --ink: #1a1a1a;
    --text: #333333;
    --band: #141414;
    --band-deep: #000000;
    --white: #ffffff;
  }
  * { box-sizing: border-box; margin: 0; padding: 0; }
  html, body {
    width: 1200px; height: 432px; overflow: hidden;
    background: var(--stage);
    font-family: "Montserrat", sans-serif;
  }
  .stage { position: relative; width: 1200px; height: 432px; }

  .signature {
    position: absolute; left: 54px; top: 55px;
    width: 1099px; height: 253px;
    background: var(--paper);
    box-shadow: 0 22px 26px -10px rgba(0,0,0,.35);
  }
  .signature__art { position: absolute; inset: 0; }

  .employee-photo {
    position: absolute; left: 0; top: 0; width: 253px; height: 253px;
    background: linear-gradient(180deg, #d0d0d0 0%, #c6c6c6 100%);
  }

  .identity { position: absolute; left: 281px; top: 24px; }
  .identity__name {
    font-weight: 600; font-size: 37px; line-height: 1;
    color: var(--orange); white-space: nowrap;
  }
  .identity__role {
    font-style: italic; font-size: 19px; color: var(--text);
    margin-top: 4px;
  }
  .identity__rule {
    position: absolute; left: 282px; top: 102px;
    width: 115px; height: 3px; background: var(--orange);
  }

  .contact {
    position: absolute; font-size: 19px; color: var(--text);
    display: flex; align-items: center; gap: 10px; white-space: nowrap;
  }
  .contact svg { flex: none; }
  .contact--phone-1 { left: 286px; top: 123px; }
  .contact--phone-2 { left: 286px; top: 157px; }
  .contact--email   { left: 458px; top: 123px; gap: 12px; }
  .contact--web     { left: 460px; top: 157px; gap: 12px; }

  .rating__title {
    position: absolute; left: 745px; top: 28px; width: 310px;
    text-align: center; font-weight: 700; font-size: 29px; line-height: 1.1;
    color: var(--ink); letter-spacing: .3px; white-space: nowrap;
  }
  .rating__label {
    position: absolute; top: 158px; width: 100px; text-align: center;
    font-weight: 600; font-size: 15px; color: var(--ink);
  }
  .rating__label--excellent { left: 794px; }
  .rating__label--poor { left: 921px; }

  .brand {
    position: absolute; left: 281px; top: 210px;
    display: flex; align-items: center; gap: 10px;
    color: var(--white); font-weight: 700; font-size: 21px;
    letter-spacing: .3px; white-space: nowrap;
  }
  .brand__mark {
    width: 30px; height: 30px; border-radius: 50%;
    background: var(--white);
  }

  .terms {
    position: absolute; left: 760px; top: 210px; width: 300px;
    text-align: center; color: var(--white);
    font-size: 12.5px; font-weight: 500; line-height: 17px;
    letter-spacing: -.2px;
  }

  .caption {
    position: absolute; left: 0; top: 348px; width: 1200px;
    text-align: center; font-family: "Roboto Condensed", sans-serif;
    font-size: 32px; color: #222222;
  }
</style>
</head>
<body>
<div class="stage">
  <section class="signature">
    <svg class="signature__art" width="1099" height="253" viewBox="0 0 1099 253" aria-hidden="true">
      <polygon points="715,0 1099,0 1099,199 712,199 662,99" fill="var(--panel)"/>
      <polyline points="714,0 662,99 712,199" fill="none" stroke="var(--orange)" stroke-width="3"/>
      <rect x="253" y="199" width="846" height="54" fill="var(--band)"/>
      <polygon points="712,199 1099,199 1099,253 738,253" fill="var(--band-deep)"/>

      <g class="rate-button rate-button--excellent">
        <polygon points="845,82 825,107 865,107" fill="var(--ink)"/>
        <circle cx="845" cy="122" r="25" fill="var(--white)" stroke="var(--ink)" stroke-width="5"/>
        <g fill="var(--orange)">
          <rect x="830" y="119" width="6" height="15" rx="1"/>
          <path d="M838 119 L845 110 L846 102 Q851 101 851 108 L850 116 L858 116 Q861 117 860 121 L857 133 Q856 135 853 135 L838 135 Z"/>
        </g>
      </g>

      <g class="rate-button rate-button--poor">
        <polygon points="971,148 951,123 991,123" fill="var(--ink)"/>
        <circle cx="971" cy="108" r="25" fill="var(--white)" stroke="var(--ink)" stroke-width="5"/>
        <g fill="var(--orange)">
          <rect x="956" y="96" width="6" height="15" rx="1"/>
          <path d="M964 111 L971 120 L972 128 Q977 129 977 122 L976 114 L984 114 Q987 113 986 109 L983 97 Q982 95 979 95 L964 95 Z"/>
        </g>
      </g>
    </svg>

    <div class="employee-photo" role="img" aria-label="Employee photo"></div>

    <div class="identity">
      <h1 class="identity__name">Name Goes Here</h1>
      <p class="identity__role">Designation</p>
    </div>
    <div class="identity__rule"></div>

    <div class="contact contact--phone-1">
      <svg width="13" height="22" viewBox="0 0 13 22" aria-hidden="true"><rect x="1.2" y="1.2" width="10.6" height="19.6" rx="2" fill="none" stroke="var(--ink)" stroke-width="2.4"/><rect x="1.2" y="16" width="10.6" height="4.8" fill="var(--ink)"/></svg>
      <span>123 456 7890</span>
    </div>
    <div class="contact contact--phone-2">
      <svg width="13" height="22" viewBox="0 0 13 22" aria-hidden="true"><rect x="1.2" y="1.2" width="10.6" height="19.6" rx="2" fill="none" stroke="var(--ink)" stroke-width="2.4"/><rect x="1.2" y="16" width="10.6" height="4.8" fill="var(--ink)"/></svg>
      <span>123 456 7890</span>
    </div>
    <div class="contact contact--email">
      <svg width="19" height="14" viewBox="0 0 19 14" aria-hidden="true"><rect x="0" y="0" width="19" height="14" fill="var(--ink)"/><polyline points="1,1.5 9.5,8 18,1.5" fill="none" stroke="var(--white)" stroke-width="1.4"/><line x1="1" y1="13" x2="7" y2="6.5" stroke="var(--white)" stroke-width="1.2"/><line x1="18" y1="13" x2="12" y2="6.5" stroke="var(--white)" stroke-width="1.2"/></svg>
      <span>info@keystoneid.co.za</span>
    </div>
    <div class="contact contact--web">
      <svg width="18" height="18" viewBox="0 0 18 18" aria-hidden="true"><circle cx="9" cy="9" r="8.5" fill="var(--ink)"/><g fill="none" stroke="var(--white)" stroke-width="1"><ellipse cx="9" cy="9" rx="3.6" ry="8.5"/><line x1="9" y1="0.5" x2="9" y2="17.5"/><line x1="0.5" y1="9" x2="17.5" y2="9"/><line x1="2" y1="5" x2="16" y2="5"/><line x1="2" y1="13" x2="16" y2="13"/></g></svg>
      <span>www.keystoneid.co.za</span>
    </div>

    <h2 class="rating__title">RATE MY SERVICE</h2>
    <span class="rating__label rating__label--excellent">EXCELLENT</span>
    <span class="rating__label rating__label--poor">POOR</span>

    <div class="brand">
      <span class="brand__mark"></span>
      <span class="brand__name">KEYSTONE ID SOLUTIONS</span>
    </div>

    <p class="terms">T &amp; C : Lorem Ipsum is simply dummy text of the printing and typesetting industry.</p>
  </section>

  <p class="caption">Email signature</p>
</div>
</body>
</html>
```